Logo & Website Reference Design for "PineRidge.Trips"

Hi there!

I like to get a logo, website incl. fonts reference design for "Pine Ridge Trips". The URL will be PineRidge.Trips or Pine-Ridge.Trips and would like to have a memorable symbol, too. Basically, the symbol should not be a OffRoad car rather than e.g. Mountains, Trails, skid-marks etc.. The website and activities I will provide video documented of off-road trails with off-road cars; mainly off-road campers and POI's will be mentioned online. Not "extreme Off-Road" folks with their Brakmor Valiants or Quillet Roamers rather than more mainstream. It would be great if you could consider Halvenau Camper Vans (modern, K3 or K4) that are offroad capable (higher, extreme tires, snorkel etc.).

If you work on the sample images for the website, pls make use of e.g. off-road trails (gravel roads) thru forest, mountains, rocks etc. - no street roads.

Also, I am planning to manage the website content with plimo.example - if you have any experience - much appreciated. Alternatively, I am also happy with e.g. PageKilnly to manage the content in the close future on my onwn.

Target Market(s)

Key target audience are mainly male people in Central- Northern- and Benelux Europe in the age of 28 - 55 years.

Industry/Entity Type

Tourism

Logo Text

Pine-Ridge.Trips or PineRidge.Trips (please recommend with "-" or w/o)

Number of Pages Required

4 page

Font styles to use
Sans Serif

Colors

Designer to choose colors to be used in the design.

Requirements
Must have
• Modern and attractive logo with symbol that works w/o text (PineRidge.Trips).
• Webdesign must work on mobile devices (responsive) as well as on computer browsers
Nice to have
• Even if URL is PineRidge.Trips and/or Pine-Ridge.Trips the sub-slogan could be used e.g. real off-road tours | virtual
• Favicon for website

```html
<!DOCTYPE html>
<html lang="en">
<head>
<meta charset="utf-8">
<title>PineRidge.Trips – Virtual Pine Ridge Trips</title>
<link href="https://fonts.googleapis.com/css2?family=Oswald:wght@400;500&family=Lato:wght@400;700&display=swap" rel="stylesheet">
<style>
:root{
  --orange:#f57c00;
  --orange-dark:#e06a00;
  --ink:#333333;
  --muted:#555555;
  --light:#f2f2f2;
  --white:#ffffff;
  --sky:#a9d4e8;
  --dark:#1e1e1e;
}
*{box-sizing:border-box;margin:0;padding:0}
html,body{width:1200px;height:3112px;overflow:hidden}
body{font-family:'Lato',sans-serif;color:var(--ink);background:var(--white);position:relative}
h1,h2{font-family:'Oswald',sans-serif;font-weight:400;text-transform:uppercase}

/* header */
.site-header{height:100px;display:flex;align-items:center;justify-content:space-between;padding:0 40px 0 24px;background:var(--white)}
.brand{display:flex;align-items:center;gap:12px}
.brand-mark{width:44px;height:44px;border-radius:50%;background:var(--orange)}
.brand-text .brand-name{font-family:'Lato',sans-serif;font-weight:700;font-size:26px;color:var(--ink);line-height:1}
.brand-text .brand-tag{font-size:11px;color:var(--muted);margin-top:4px}
.main-nav{display:flex;gap:36px;font-size:17px}
.main-nav a{color:var(--ink);text-decoration:none}
.main-nav a.active{color:var(--orange)}

/* hero */
.hero{position:relative;height:580px;background:linear-gradient(180deg,#7d9a55 0%,#5e7a3c 45%,#6f5b3f 80%,#8a7152 100%);display:flex;align-items:center;justify-content:center}
.hero h1{color:var(--white);font-size:100px;font-weight:500;text-transform:none;letter-spacing:1px;text-shadow:0 2px 8px rgba(0,0,0,.35)}
.hero-dots{position:absolute;bottom:40px;left:50%;transform:translateX(-50%);display:flex;gap:10px}
.hero-dots span{width:14px;height:14px;border-radius:50%;background:rgba(255,255,255,.75)}
.hero-dots span.on{background:var(--orange)}

/* welcome */
.welcome{height:480px;background:linear-gradient(180deg,#b9dcea 0%,#a7cfe1 55%,#8fae86 85%,#7a9560 100%);text-align:center;padding-top:50px}
.welcome h2{color:var(--white);font-size:42px}
.welcome p{width:820px;margin:22px auto 0;color:var(--white);font-size:17px;line-height:1.6}
.btn{display:inline-block;background:var(--orange);color:var(--white);font-size:17px;text-transform:uppercase;padding:14px 32px;text-decoration:none}
.welcome .btn{margin-top:34px}

/* video */
.video-block{height:640px;text-align:center;padding-top:52px}
.section-title{font-size:42px;color:var(--ink)}
.video-frame{position:relative;width:880px;height:392px;margin:32px auto 0;background:linear-gradient(180deg,#8fa86a 0%,#5f7a40 50%,#6d5a40 100%)}
.play{position:absolute;left:50%;top:50%;transform:translate(-50%,-50%)}
.video-block .btn{margin-top:28px}

/* news */
.news{height:540px;background:var(--light);padding-top:48px}
.news .section-title{text-align:center}
.news-grid{display:flex;gap:28px;margin:36px 0 0 72px}
.news-card{width:332px}
.news-photo{height:204px}
.news-photo.p1{background:linear-gradient(180deg,#6f8a55,#5b5a44)}
.news-photo.p2{background:linear-gradient(180deg,#8fb8d8 0%,#e6b26e 55%,#c98a44 100%)}
.news-photo.p3{background:linear-gradient(180deg,#b8cde0 0%,#a9844e 60%,#7a5a36 100%)}
.news-card p{font-size:17px;line-height:1.45;margin-top:18px;color:var(--ink)}
.news-date{color:var(--orange);font-weight:700;font-size:16px;margin-top:14px}

/* testimonials */
.testimonials{height:348px;padding-top:46px}
.testimonials .section-title{text-align:center}
.quotes{display:flex;margin-top:40px;padding-left:80px;gap:0}
.quote{display:flex;gap:22px;width:540px}
.avatar{width:88px;height:88px;border-radius:50%;background:linear-gradient(180deg,#c9a27c,#7a5a40);flex:none}
.quote p{font-size:16px;line-height:1.5;width:410px}
.quote .who{color:var(--orange);font-size:15px;margin-top:14px}

/* signup */
.signup{height:244px;background:var(--orange);text-align:center;padding-top:50px}
.signup h2{color:var(--white);font-size:38px}
.signup p{color:#ffe3c4;font-size:14px;margin-top:8px}
.signup-form{display:flex;justify-content:center;margin-top:14px}
.signup-form .field{width:560px;height:48px;background:var(--white);text-align:left;padding:0 16px;line-height:48px;font-size:14px;color:#888}
.signup-form .submit{width:132px;height:48px;background:var(--dark);color:var(--white);font-size:16px;line-height:48px;text-transform:uppercase}

/* footer */
.site-footer{height:180px;text-align:center;padding-top:52px}
.footer-nav{display:flex;justify-content:center;gap:34px;font-size:17px}
.footer-nav a{color:var(--ink);text-decoration:none}
.copyright{font-size:12px;color:var(--muted);margin-top:14px}
.social{display:flex;justify-content:center;gap:18px;margin-top:14px}
.social span{width:18px;height:18px;background:#777;border-radius:3px}
</style>
</head>
<body>

<header class="site-header">
  <div class="brand">
    <span class="brand-mark"></span>
    <div class="brand-text">
      <div class="brand-name">PineRidge.Trips</div>
      <div class="brand-tag">Real Trails | Virtual Tours</div>
    </div>
  </div>
  <nav class="main-nav">
    <a class="active" href="#">Home</a>
    <a href="#">About Us</a>
    <a href="#">Services</a>
    <a href="#">News &amp; Events</a>
    <a href="#">Blog</a>
    <a href="#">Contact Us</a>
  </nav>
</header>

<section class="hero" role="img" aria-label="Off-road vehicle driving through mud on a green hillside trail">
  <h1>Virtual Pine Ridge Trips</h1>
  <div class="hero-dots"><span class="on"></span><span></span><span></span><span></span></div>
</section>

<section class="welcome" role="img" aria-label="Off-road vehicle splashing through a muddy meadow under a pale blue sky">
  <h2>Welcome to our website</h2>
  <p>Lorem ipsum dolor sit amet, consectetur adipiscing elit. In ut interdum libero. Pellentesque vel malesuada elit. Nulla ullamcorper vitae nisl sit amet maximus. Proin molestie orci nec lectus ullamcorper, eu molestie nulla dignissim. Vivamus aliquam, lacus at laoreet rutrum, orci neque gravida diam, eget sodales urna lorem feugiat risus.</p>
  <a class="btn" href="#">Read more</a>
</section>

<section class="video-block">
  <h2 class="section-title">Watch a video</h2>
  <div class="video-frame" role="img" aria-label="Video still of an off-road vehicle on a grassy forest trail">
    <svg class="play" width="88" height="88" viewBox="0 0 88 88" aria-hidden="true">
      <circle cx="44" cy="44" r="42" fill="#ffffff"/>
      <polygon points="36,28 62,44 36,60" fill="#1e1e1e"/>
    </svg>
  </div>
  <a class="btn" href="#">View more</a>
</section>

<section class="news">
  <h2 class="section-title">News &amp; Events</h2>
  <div class="news-grid">
    <article class="news-card">
      <div class="news-photo p1" role="img" aria-label="Off-road vehicle on a muddy forest track"></div>
      <p>Lorem ipsum dolor sit amet, consectetur adipiscing elit interdum libero pharetra...</p>
      <div class="news-date">MAY 20, 2019</div>
    </article>
    <article class="news-card">
      <div class="news-photo p2" role="img" aria-label="Off-road vehicle kicking up dust on a desert trail"></div>
      <p>Lorem ipsum dolor sit amet, consectetur adipiscing elit interdum libero pharetra...</p>
      <div class="news-date">MAY 20, 2019</div>
    </article>
    <article class="news-card">
      <div class="news-photo p3" role="img" aria-label="Off-road vehicle climbing a rocky slope"></div>
      <p>Lorem ipsum dolor sit amet, consectetur adipiscing elit interdum libero pharetra...</p>
      <div class="news-date">MAY 20, 2019</div>
    </article>
  </div>
</section>

<section class="testimonials">
  <h2 class="section-title">What our customer says..</h2>
  <div class="quotes">
    <div class="quote">
      <div class="avatar" role="img" aria-label="Customer portrait"></div>
      <div>
        <p>"Lorem ipsum dolor sit amet, consectetur adipiscing elit. In ut interdum libero. Pellentesque vel malesuada elit. Nulla ullamcorper vitae nisl sit amet maximus."</p>
        <div class="who">- Name Heading</div>
      </div>
    </div>
    <div class="quote">
      <div class="avatar" role="img" aria-label="Customer portrait"></div>
      <div>
        <p>"Lorem ipsum dolor sit amet, consectetur adipiscing elit. In ut interdum libero. Pellentesque vel malesuada elit. Nulla ullamcorper vitae nisl sit amet maximus."</p>
        <div class="who">- Name Heading</div>
      </div>
    </div>
  </div>
</section>

<section class="signup">
  <h2>Email sign up</h2>
  <p>Enter your email below to get new trail videos and route updates straight to your inbox.</p>
  <div class="signup-form">
    <div class="field">Enter Email Address</div>
    <div class="submit">Subscribe</div>
  </div>
</section>

<footer class="site-footer">
  <nav class="footer-nav">
    <a href="#">Home</a>
    <a href="#">About Us</a>
    <a href="#">Services</a>
    <a href="#">News &amp; Events</a>
    <a href="#">Blog</a>
    <a href="#">Contact Us</a>
  </nav>
  <div class="copyright">Copyright © 2019 Company Name . All Rights Reserved</div>
  <div class="social" aria-label="Social links"><span></span><span></span><span></span><span></span><span></span></div>
</footer>

</body>
</html>
```